Logo and packaging design for Lime restoration mortar

We need a logo and packaging design for out line of restoration profits. This includes labels for pales, and cement bags. I have attached out current logo. And a design from you that I really like. This is the kind of colour scheme and style I would like for our packaging.

I would like a new logo that is similar, or related to our existing but more presentable in a retail environment. I think a mark is also necessary for the logo. Currently it is just words and that makes branding a bit difficult.

Target Market(s)

DIYers we will be selling to hardware stores

Logo Text

Fernlow

Requirements
Must have
• Logo and packaging template that uses the new logo.
Nice to have
• I really like impactful logos. I love the crown logo, however I would prefer not to copy it. I would like a impactful logo, that can be easily broken down for branding different products.

```html
<!DOCTYPE html>
<html lang="en">
<head>
<meta charset="utf-8">
<title>Fernlow Lime Restoration Mortar – Bag Front</title>
<link href="https://fonts.googleapis.com/css2?family=Saira+Semi+Condensed:wght@600;800&display=swap" rel="stylesheet">
<style>
  :root {
    --bg: #e9eaea;
    --bag-white: #ffffff;
    --brand-green: #6cc24a;
    --brand-green-light: #74cf4e;
    --ink-white: #ffffff;
    --mark-tint: #f4fbf0;
    --text-font: "Saira Semi Condensed", "Arial Narrow", Arial, sans-serif;
  }
  * { margin: 0; padding: 0; box-sizing: border-box; }
  html, body {
    width: 1200px; height: 675px; overflow: hidden;
    background: var(--bg);
    font-family: var(--text-font);
  }
  .canvas { position: relative; width: 1200px; height: 675px; }
  .bag-front {
    position: absolute; left: 385px; top: 20px;
    width: 430px; height: 636px;
    background: var(--bag-white);
    box-shadow: 0 6px 18px rgba(0,0,0,0.12);
  }
  .label-panel {
    position: absolute; left: 19px; top: 33px;
    width: 397px; height: 589px;
    background: linear-gradient(160deg, var(--brand-green) 0%, var(--brand-green-light) 100%);
  }
  .hero-mark-area {
    position: absolute; left: 19px; top: 47px;
    width: 264px; height: 400px;
    background: linear-gradient(170deg, var(--mark-tint) 0%, #ffffff 100%);
    opacity: 0.92;
  }
  .brand-lockup {
    position: absolute; left: 281px; top: 62px;
    width: 110px; text-align: center;
    color: var(--ink-white);
  }
  .brand-lockup .brand-square {
    display: block; width: 40px; height: 40px; margin: 0 auto 10px;
    background: var(--ink-white);
  }
  .brand-lockup .brand-name {
    display: block;
    font-weight: 600; font-size: 13px; letter-spacing: 3px;
    text-transform: uppercase;
  }
  .feature-list {
    position: absolute; left: 306px; top: 139px;
    width: 90px; list-style: none;
  }
  .feature {
    position: absolute; left: 0; width: 90px; text-align: center;
    color: var(--ink-white);
  }
  .feature svg { display: block; margin: 0 auto; }
  .feature .feature-label {
    display: block; margin-top: 5px;
    font-weight: 800; font-size: 5.5px; line-height: 1.1;
    text-transform: uppercase; letter-spacing: 0.2px;
  }
  .feature.weather { top: 34px; }
  .feature.mortar { top: 123px; }
  .feature.plaster { top: 205px; }
  .feature.workability { top: 287px; }
  .divider {
    position: absolute; left: 19px; top: 476px;
    width: 264px; height: 4px; background: var(--ink-white);
  }
  .product-name {
    position: absolute; left: 33px; top: 496px;
    color: var(--ink-white); text-transform: uppercase; line-height: 1;
  }
  .product-name .line-1 { display: block; font-weight: 800; font-size: 22px; letter-spacing: 0.6px; }
  .product-name .line-2 { display: block; font-weight: 800; font-size: 46px; margin-top: 2px; letter-spacing: 0.5px; }
  .weight-tag {
    position: absolute; left: 305px; top: 528px;
    width: 79px; height: 94px;
    background: var(--bag-white);
    display: flex; align-items: center; justify-content: center;
    color: var(--brand-green);
    font-weight: 800; font-size: 22px; padding-top: 24px;
  }
</style>
</head>
<body>
<div class="canvas">
  <div class="bag-front">
    <div class="label-panel"></div>

    <div class="hero-mark-area" role="img" aria-label="Large Fernlow brand mark decoration in white on the green label"></div>

    <div class="brand-lockup">
      <span class="brand-square"></span>
      <span class="brand-name">Fernlow</span>
    </div>

    <ul class="feature-list">
      <li class="feature weather">
        <svg width="52" height="52" viewBox="0 0 52 52" fill="none" stroke="#fff" stroke-width="2.4" stroke-linecap="round">
          <circle cx="26" cy="26" r="24"/>
          <path d="M17 28 a5 5 0 0 1 2-9 a7 7 0 0 1 13-1 a5 5 0 0 1 3 10 z" stroke-width="2"/>
          <path d="M18 32 l-2 4 M23 32 l-2 4 M28 32 l-2 4 M33 32 l-2 4" stroke-width="1.6"/>
        </svg>
        <span class="feature-label">Weather proof<br>packaging</span>
      </li>
      <li class="feature mortar">
        <svg width="52" height="52" viewBox="0 0 52 52" fill="none" stroke="#fff" stroke-width="2.4">
          <circle cx="26" cy="26" r="24"/>
          <g fill="#fff" stroke="none">
            <rect x="15" y="16" width="10" height="4"/><rect x="27" y="16" width="10" height="4"/>
            <rect x="15" y="22" width="5" height="4"/><rect x="22" y="22" width="9" height="4"/><rect x="33" y="22" width="4" height="4"/>
            <rect x="15" y="28" width="10" height="4"/><rect x="27" y="28" width="10" height="4"/>
            <rect x="15" y="34" width="5" height="4"/><rect x="22" y="34" width="9" height="4"/><rect x="33" y="34" width="4" height="4"/>
          </g>
        </svg>
        <span class="feature-label">Mortar</span>
      </li>
      <li class="feature plaster">
        <svg width="52" height="52" viewBox="0 0 52 52" fill="none" stroke="#fff" stroke-width="2.4">
          <circle cx="26" cy="26" r="24"/>
          <path d="M16 30 L30 16 L36 22 L22 36 Z" fill="#fff" stroke="none"/>
          <path d="M31 20 L37 14" stroke-width="3" stroke-linecap="round"/>
        </svg>
        <span class="feature-label">Plaster</span>
      </li>
      <li class="feature workability">
        <svg width="52" height="52" viewBox="0 0 52 52" fill="none" stroke="#fff" stroke-width="2.4">
          <circle cx="26" cy="26" r="24"/>
          <path d="M16 28 L28 24 L24 36 Z" fill="#fff" stroke="none"/>
          <path d="M26 26 L36 16" stroke-width="3" stroke-linecap="round"/>
        </svg>
        <span class="feature-label">Improved<br>workability</span>
      </li>
    </ul>

    <div class="divider"></div>

    <h1 class="product-name">
      <span class="line-1">Lime Restoration</span>
      <span class="line-2">Mortar</span>
    </h1>

    <div class="weight-tag">50KG</div>
  </div>
</div>
</body>
</html>
```